wedding photography website for top wedding photographer

I have a website right now that is barely working. I want the photos to maybe all the photos lined up horizontally and you scroll to see the images. I have an orange logo and want it to be dark grey. I also need a page for publications (I have those as scans) and a link to an About page.

Target Market(s)

wedding planners and bride

Industry/Entity Type

Wedding Photography

Coding

Coded - Design and coding required

Number of Pages Required

5+ page

Font styles to use
Serif
Sans Serif

Colors
ffffff
474747

Requirements
Must have
• easy to navigate, always want the instagram and contact info readily available, should be clean and modern and let the photos stand out. it's wedding photos but i don't want it to feel girly or prissy.
Nice to have
• possibly could be one big photo on the home page, then click it to go into all the other photos. want page options on the home page and every page
Should not have
• nothing fussy or quaint, want this to be the "Copper Ladle" restaurant of wedding photography

```html
<!DOCTYPE html>
<html lang="en">
<head>
<meta charset="utf-8">
<title>Ava Lennox Photography</title>
<link rel="stylesheet" href="https://fonts.googleapis.com/css2?family=Poppins:wght@300;400;500;600&display=swap">
<style>
:root{
  --white:#ffffff;
  --ink:#474747;
  --dark:#2b2b2b;
  --text:#555555;
  --muted:#777777;
  --panel:#efefef;
  --field:#f2f2f2;
}
*{box-sizing:border-box;margin:0;padding:0}
html,body{width:1200px;height:3103px;overflow:hidden}
body{font-family:'Poppins',sans-serif;color:var(--text);background:var(--white);position:relative}
.abs{position:absolute}
.photo{position:absolute;display:block}

/* hero */
.hero{position:absolute;left:0;top:0;width:1200px;height:610px;
  background:radial-gradient(ellipse at 62% 40%,#6b665c 0%,#3b3832 38%,#1e1d1a 75%,#141412 100%)}
.brand{position:absolute;font-family:'Poppins',sans-serif;font-weight:300;font-size:22px;letter-spacing:.5px}
.hero .brand{left:165px;top:44px;color:var(--white)}
.nav{position:absolute;left:610px;top:48px;display:flex;gap:0}
.nav a{color:var(--white);text-decoration:none;font-size:13px;margin-right:28px;padding-bottom:4px}
.nav a.active{border-bottom:1px solid var(--white)}
.social{position:absolute;left:958px;top:52px;display:flex;gap:14px}
.social span{width:13px;height:13px;border-radius:50%;background:var(--white);display:block}
.hero h1{position:absolute;left:161px;top:222px;color:var(--white);font-weight:400;font-size:46px;line-height:58px}
.hero h1 strong{font-weight:500}
.hero .lead{position:absolute;left:161px;top:344px;color:var(--white);font-size:15px;font-weight:300}
.btn-dark{position:absolute;left:161px;top:391px;width:166px;height:44px;border-radius:22px;background:#3d3d3d;color:var(--white);font-size:13px;display:flex;align-items:center;justify-content:center}
.arrow{position:absolute;top:322px}

/* about */
.about-photo{left:161px;top:662px;width:362px;height:399px;background:linear-gradient(135deg,#2a211c,#4a3b2e 55%,#8a8170)}
.section-title{font-weight:300;font-size:31px;color:#333}
.about h2{position:absolute;left:571px;top:696px}
.about p{position:absolute;left:571px;top:762px;width:460px;font-size:11.5px;line-height:18.6px;color:var(--text)}
.signature{left:566px;top:970px;width:160px;height:66px;background:linear-gradient(90deg,#e6e6e6,#f6f6f6)}
.rule{position:absolute;left:0;top:1119px;width:1200px;height:1px;background:#e2e2e2}

/* works */
.works{position:absolute;left:0;top:1124px;width:1200px;height:869px;background:var(--panel)}
.works h2{position:absolute;left:0;width:1200px;top:26px;text-align:center}
.works p{position:absolute;left:255px;width:690px;top:90px;text-align:center;font-size:11.5px;line-height:21px}

/* blog */
.blog h2{position:absolute;left:0;width:1200px;top:2034px;text-align:center}
.card{position:absolute;top:2112px;width:271px;height:421px;background:var(--white);box-shadow:0 10px 30px rgba(0,0,0,.12)}
.card .photo{left:0;top:0;width:100%;height:199px}
.card h3{position:absolute;left:18px;top:218px;width:240px;font-size:13px;font-weight:600;line-height:23px;color:#222}
.card time{position:absolute;left:18px;top:282px;font-size:11px;color:var(--muted)}
.card p{position:absolute;left:18px;top:306px;width:230px;font-size:11px;line-height:21px;color:var(--muted)}
.card a{position:absolute;left:18px;top:378px;font-size:12px;color:#222;text-decoration:none}

/* contact */
.contact{position:absolute;left:0;top:2590px;width:1200px;height:358px;background:radial-gradient(ellipse at 30% 60%,#5a5a5a,#3d3d3d 60%,#333 100%)}
.contact h2{position:absolute;left:0;width:1200px;top:36px;text-align:center;color:var(--white);font-weight:300;font-size:30px}
.field{position:absolute;left:412px;width:376px;background:var(--field);font-size:11px;color:#888;padding:8px 12px}
.btn-line{position:absolute;left:526px;top:273px;width:148px;height:36px;border:1px solid var(--white);border-radius:18px;color:var(--white);font-size:11px;display:flex;align-items:center;justify-content:center;letter-spacing:.5px}

/* footer */
.footer{position:absolute;left:0;top:2948px;width:1200px;height:155px;background:var(--dark);text-align:center;color:var(--white)}
.footer .brand{position:static;display:block;margin-top:32px}
.footer nav{margin-top:14px;font-size:12px}
.footer small{display:block;margin-top:12px;font-size:11px}
</style>
</head>
<body>

<header class="hero" role="img" aria-label="Photo of a bride and groom embracing outdoors at dusk">
  <div class="brand">Ava Lennox Photography</div>
  <nav class="nav">
    <a class="active">Home</a><a>About</a><a>Clients</a><a>Portfolio</a><a>Blog</a>
  </nav>
  <div class="social" aria-label="Social links"><span></span><span></span><span></span></div>
  <h1>Hello,<br>I'm <strong>Ava Lennox</strong></h1>
  <div class="lead">Neque porro quisuam est qui dodolor sit amet,</div>
  <div class="btn-dark">See My Works</div>
  <svg class="arrow" style="left:36px" width="24" height="26" viewBox="0 0 24 26" fill="none" stroke="#ddd" stroke-width="1.5"><path d="M12 2L2 13l10 11M22 2L12 13l10 11"/></svg>
  <svg class="arrow" style="left:1140px" width="24" height="26" viewBox="0 0 24 26" fill="none" stroke="#ddd" stroke-width="1.5"><path d="M2 2l10 11L2 24M12 2l10 11-10 11"/></svg>
</header>

<section class="about">
  <div class="photo about-photo" role="img" aria-label="Photographer standing beside a long banquet table set for a wedding"></div>
  <h2 class="section-title">About MySelf</h2>
  <p>Lorem ipsum dolor sit amet, consectetur adipiscing elit, sed do eiusmod tempor incididunt ut labore et dolore magna aliqua. Ut enim ad minim veniam, quis nos trud exercitation ullamco laboris nisi ut aliquip ex ea commodo consequat. Duis aute irure dolor in reprehenderit in voluptate velit esse cillum dolore eu fugiat null a pariatur. Excepteur sint occaecat cupidatat non proident, sunt in culpa qui offi cia deserunt mollit anim id est aute irure dolor in reprehenderit in voluptate velit esse cillum dolore eu fugiat nulla pariatur. Excepteur sint occaecat cupidatat non proident, sunt in culpa qui officia deserunt mollit anim id est</p>
  <div class="photo signature" role="img" aria-label="Handwritten signature"></div>
</section>
<div class="rule"></div>

<section class="works">
  <h2 class="section-title">My Works</h2>
  <p>Lorem ipsum dolor sit amet, consectetur adipiscing elit, sed do eiusmod tempor incididunt ut labore et dolore magnua enim ad minim veniam, quis nostrud exercitation ullamco laboris nisi ut aliquip ex ea commodo consequat.uis aute irure dolor in reprehenderit in voluptate velit esse cillum dolore eu fugiat nulla pariatur. Excepteur sint occaecat</p>
</section>
<div class="photo" style="left:161px;top:1312px;width:307px;height:380px;background:linear-gradient(180deg,#c9cfc0,#8f9a6a 55%,#5f6b38)" role="img" aria-label="Couple standing in a wildflower meadow"></div>
<div class="photo" style="left:476px;top:1312px;width:401px;height:198px;background:linear-gradient(90deg,#8fae5a,#d9d4c8 50%,#6f8f3e)" role="img" aria-label="Bride and groom close together with a pink bouquet"></div>
<div class="photo" style="left:886px;top:1312px;width:153px;height:198px;background:linear-gradient(180deg,#5d7a3a,#a8a48a 60%,#7b8a5a)" role="img" aria-label="Couple embracing by a garden gate"></div>
<div class="photo" style="left:476px;top:1519px;width:277px;height:200px;background:linear-gradient(180deg,#e8e6e0,#b9c79c 60%,#d8d4c8)" role="img" aria-label="Bride holding a lily of the valley bouquet"></div>
<div class="photo" style="left:763px;top:1519px;width:276px;height:200px;background:linear-gradient(180deg,#9a5a44,#6a3e30 50%,#3a2a24)" role="img" aria-label="Couple at an arched brick doorway"></div>
<div class="photo" style="left:161px;top:1701px;width:307px;height:221px;background:linear-gradient(180deg,#d6d8d6,#a9aeb0 55%,#6d6a64)" role="img" aria-label="Groom kneeling to kiss the bride by the water"></div>
<div class="photo" style="left:476px;top:1728px;width:563px;height:194px;background:linear-gradient(90deg,#3a3a3a,#9a9a96 45%,#e8e8e4 80%,#cfcfcb)" role="img" aria-label="Couple smiling in the back seat of a car"></div>

<section class="blog">
  <h2 class="section-title">Blog Posts</h2>
  <article class="card" style="left:161px">
    <div class="photo" style="background:linear-gradient(180deg,#a7b08a,#6f7a52 60%,#4a4a3e)" role="img" aria-label="Couple walking hand in hand in a park"></div>
    <h3>Lorem ipsum dolor sit amet cons ectetur adipiscing elit so</h3>
    <time>May 3, 2018</time>
    <p>Sed ut perspiciatis unde omnis iste natus error sit lao hoksi voluptatem llos mukatu doisa nojllaud aperiam.</p>
    <a>Read More</a>
  </article>
  <article class="card" style="left:465px">
    <div class="photo" style="background:linear-gradient(180deg,#7f9a5a,#d8b0b0 55%,#c46a7a)" role="img" aria-label="Bridesmaids helping the bride with her dress"></div>
    <h3>Lorem ipsum dolor sit amet cons ectetur adipiscing elit so</h3>
    <time>May 3, 2018</time>
    <p>Sed ut perspiciatis unde omnis iste natus error sit lao hoksi voluptatem llos mukatu doisa nojllaud aperiam.</p>
    <a>Read More</a>
  </article>
  <article class="card" style="left:768px">
    <div class="photo" style="background:linear-gradient(180deg,#4a3a2e,#8a6a4a 50%,#2e2824)" role="img" aria-label="Candlelit wedding ceremony with guests"></div>
    <h3>Lorem ipsum dolor sit amet cons ectetur adipiscing elit so</h3>
    <time>May 3, 2018</time>
    <p>Sed ut perspiciatis unde omnis iste natus error sit lao hoksi voluptatem llos mukatu doisa nojllaud aperiam.</p>
    <a>Read More</a>
  </article>
</section>

<section class="contact" role="img" aria-label="Muted black and white photo of a bride in the background">
  <h2>Let's Talk?</h2>
  <div class="field" style="top:104px;height:34px">*Your name</div>
  <div class="field" style="top:147px;height:34px">*Your Email</div>
  <div class="field" style="top:191px;height:64px">Message</div>
  <div class="btn-line">SEND MESSAGE</div>
</section>

<footer class="footer">
  <span class="brand">Ava Lennox Photography</span>
  <nav>About &nbsp;•&nbsp; Contact &nbsp;•&nbsp; Links &nbsp;•&nbsp; Publications</nav>
  <small>© Copyright 2018. Ava Lennox Photography</small>
</footer>

</body>
</html>
```